Business card for our large format printing and installation business

We want a professional looking business card for our business. We manufacture and install Signs.

On the back of the card add this info
Large Format Graphics Printing & Installations, Event Graphics, Banners, Posters, Vehicle Fleet Graphics, Boat Wraps, Wall Murals, Decals,Displays,Signs,Plaques,Digital Signs

On the Front of the card add the Tallowfern Signs logo, plus On the back of the card add the Orange Tallowfern Wraps logo. The 2 vector logos are attached to the design brief.

Target Market(s)

Local business owners

Contact Information for Business Card

Colors
f37122
f68d4e
f9ba93

Requirements
Must have
• On the Front of the card add the Tallowfern Signs logo, plus On the back of the card add the Orange Tallowfern Wraps logo. The 2 vector logos are attached to the design brief.

```html
<!DOCTYPE html>
<html lang="en">
<head>
<meta charset="utf-8">
<title>Tallowfern Signs &amp; Wraps Business Card</title>
<link rel="stylesheet" href="https://fonts.googleapis.com/css2?family=Open+Sans:wght@400;700&family=Poppins:wght@600;800&display=swap">
<style>
  :root {
    --stage: #d3d3d3;
    --stage-light: #ececec;
    --ink: #2b2728;
    --ink-soft: #3a3536;
    --paper: #ffffff;
    --gold: #fbbf1a;
    --amber: #f7a21b;
    --orange: #f37122;
    --lemon: #fde23a;
    --text-dark: #1f1c1d;
  }
  * { box-sizing: border-box; margin: 0; padding: 0; }
  html, body { width: 900px; height: 1200px; overflow: hidden; }
  body {
    background: radial-gradient(ellipse at 50% 50%, var(--stage-light) 0%, var(--stage) 75%);
    position: relative;
    font-family: "Open Sans", Arial, sans-serif;
  }
  .card {
    position: absolute;
    left: 82px;
    width: 733px;
    height: 431px;
    border-radius: 20px;
    overflow: hidden;
    box-shadow: 0 4px 10px rgba(0,0,0,0.35);
  }
  .card--front { top: 137px; background: var(--ink); }
  .card--back { top: 633px; }
  .card__art { position: absolute; inset: 0; width: 100%; height: 100%; }

  .wordmark {
    position: absolute;
    font-family: "Poppins", Arial, sans-serif;
    font-weight: 800;
    text-align: center;
    line-height: 0.9;
    letter-spacing: 1px;
  }
  .wordmark__main { display: block; font-size: 74px; }
  .wordmark__sub { display: block; font-size: 56px; }
  .card--front .wordmark { left: 108px; top: 40px; width: 520px; color: var(--amber); }
  .card--back .wordmark { left: 100px; top: 100px; width: 540px; color: var(--ink); }

  .holder {
    position: absolute;
    right: 390px;
    top: 248px;
    text-align: right;
    color: var(--text-dark);
  }
  .holder__name { font-size: 25px; letter-spacing: 0.5px; margin-bottom: 6px; }
  .holder__name strong { font-weight: 700; }
  .holder__address { font-size: 16px; line-height: 22px; }

  .divider {
    position: absolute;
    left: 364px; top: 248px;
    width: 1.5px; height: 100px;
    background: var(--text-dark);
  }
  .contacts {
    position: absolute;
    left: 388px; top: 250px;
    list-style: none;
    font-size: 16px;
    color: var(--text-dark);
  }
  .contacts li { display: flex; align-items: center; height: 26px; }
  .contacts svg { width: 18px; height: 18px; margin-right: 9px; flex: none; }

  .services {
    position: absolute;
    left: 0; right: 0; top: 322px;
    text-align: center;
    font-family: "Poppins", Arial, sans-serif;
  }
  .services__title {
    color: var(--gold);
    font-weight: 800;
    font-size: 19px;
    letter-spacing: 0.3px;
    margin-bottom: 4px;
  }
  .services__list {
    color: var(--paper);
    font-family: "Open Sans", Arial, sans-serif;
    font-size: 17.5px;
    line-height: 27px;
  }
  .dot { color: var(--orange); padding: 0 3px; }
</style>
</head>
<body>

<section class="card card--front" aria-label="Front of card">
  <svg class="card__art" viewBox="0 0 733 431" preserveAspectRatio="none" aria-hidden="true">
    <defs>
      <linearGradient id="rim" x1="0" y1="0" x2="1" y2="0">
        <stop offset="0" stop-color="var(--lemon)"/>
        <stop offset="1" stop-color="var(--orange)"/>
      </linearGradient>
    </defs>
    <path d="M0,55 C40,140 90,182 200,188 L590,188 C650,188 700,168 733,140 L733,431 L480,431 C380,400 190,390 0,325 Z" fill="url(#rim)"/>
    <path d="M0,70 C40,152 90,194 200,200 L590,200 C650,200 700,182 733,155 L733,431 L470,431 C370,405 190,392 0,340 Z" fill="var(--paper)"/>
    <path d="M0,350 C180,405 370,410 480,431 L0,431 Z" fill="var(--ink)"/>
    <path d="M520,0 C620,10 680,60 733,95 L733,0 Z" fill="var(--ink-soft)"/>
  </svg>

  <div class="wordmark" aria-label="Tallowfern Signs">
    <span class="wordmark__main">Tallowfern</span>
    <span class="wordmark__sub">Signs</span>
  </div>

  <div class="holder">
    <p class="holder__name"><strong>MARCUS</strong> DELANEY</p>
    <p class="holder__address">1480 Harbor View Lane #7<br>Coral Bend<br>FL 33120</p>
  </div>
  <div class="divider"></div>

  <ul class="contacts">
    <li>
      <svg viewBox="0 0 18 18"><rect width="18" height="18" rx="4" fill="var(--ink)"/><path d="M5,4 L7,4 L8,7 L6.8,8 C7.6,9.6 8.6,10.6 10,11.2 L11,10 L14,11 L14,13 C14,13.6 13.5,14 13,14 C8,13.6 4.4,10 4,5 C4,4.5 4.4,4 5,4 Z" fill="var(--amber)"/></svg>
      Office: 555-310-4827
    </li>
    <li>
      <svg viewBox="0 0 18 18"><rect width="18" height="18" rx="4" fill="var(--ink)"/><path d="M5,4 L7,4 L8,7 L6.8,8 C7.6,9.6 8.6,10.6 10,11.2 L11,10 L14,11 L14,13 C14,13.6 13.5,14 13,14 C8,13.6 4.4,10 4,5 C4,4.5 4.4,4 5,4 Z" fill="var(--amber)"/></svg>
      Direct: 555-648-2093
    </li>
    <li>
      <svg viewBox="0 0 18 18"><rect width="18" height="18" rx="4" fill="var(--ink)"/><rect x="3.5" y="5" width="11" height="8" fill="var(--amber)"/><path d="M3.5,5 L9,9.5 L14.5,5" fill="none" stroke="var(--ink)" stroke-width="1.2"/></svg>
      marcus@tallowfern.net
    </li>
    <li>
      <svg viewBox="0 0 18 18"><rect width="18" height="18" rx="4" fill="var(--ink)"/><circle cx="9" cy="9" r="5.5" fill="none" stroke="var(--amber)" stroke-width="1.3"/><ellipse cx="9" cy="9" rx="2.3" ry="5.5" fill="none" stroke="var(--amber)" stroke-width="1.1"/><path d="M3.5,9 H14.5" stroke="var(--amber)" stroke-width="1.1"/></svg>
      www.Tallowfernwraps.com
    </li>
  </ul>
</section>

<section class="card card--back" aria-label="Back of card">
  <svg class="card__art" viewBox="0 0 733 431" preserveAspectRatio="none" aria-hidden="true">
    <defs>
      <linearGradient id="sun" x1="0" y1="0" x2="0" y2="1">
        <stop offset="0" stop-color="var(--lemon)"/>
        <stop offset="1" stop-color="var(--amber)"/>
      </linearGradient>
    </defs>
    <rect width="733" height="431" fill="url(#sun)"/>
    <path d="M0,0 L733,0 L733,110 C640,140 560,90 430,55 C300,20 150,40 0,85 Z" fill="var(--lemon)" opacity="0.55"/>
    <path d="M0,268 C140,232 300,252 430,276 C560,300 650,295 733,275 L733,431 L0,431 Z" fill="var(--ink)"/>
  </svg>

  <div class="wordmark" aria-label="Tallowfern Wraps">
    <span class="wordmark__main">Tallowfern</span>
    <span class="wordmark__sub">Wraps</span>
  </div>

  <div class="services">
    <p class="services__title">LARGE FORMAT GRAPHICS PRINTING &amp; INSTALLATIONS</p>
    <p class="services__list">
      Banners <span class="dot">•</span> Posters <span class="dot">•</span> Vehicle Graphics <span class="dot">•</span> Boat Wraps <span class="dot">•</span> Wall Murals <span class="dot">•</span> Decals<br>
      Displays,Signs <span class="dot">•</span> Plaques <span class="dot">•</span> Digital Signs
    </p>
  </div>
</section>

</body>
</html>
```